Business branding (card, web design) needed for Remedial / Sports massage

I need a clean, fresh design for my sports massage business called Brightwell-Motion.

I work with high profile professional sports teams (massage, clinical tapeing, health assessments, pilates, coaching) however would like to expand into the entertainment market so need a design that would appeal to both.
NO LOTUS FLOWERS, HANDS OR YOGA POSES FOR DESIGNS

The successful brand design will need to be scalable (e.g. resolution/sizing) to work holistically across my website, marketing collateral and clothing.

Colour pallets that appeal to me - Black, white, blue, green, taupe,
and would prefer clean crisp designs that evoke professionalism, continuous improvement, flow and balance.

Good Luck, can't wait to find my new brand... :)
Updates

I have uploaded a business card that I do like,  See if you can be creative with the logo

Thanks

Target Market(s)

professional sports teams / athletes, and entertainment professionals.

I HAVE UPLOADED A PDF OF WHAT I HAVE DONE. YOU MAY USE LOGO BUT BE CREATIVE PLEASE.

Industry/Entity Type

Entertainment

Contact Information for Business Card

Brightwell-Motion
'Move Stronger' (strap line)

Colette Farrow
Director / Remedial Massage

0417263950
212 Larkmore Street
Kelbridge, VIC 3261

www.brightwell-motion.com.au
info@brightwell-motion.com.au

Logo Text

Brightwell-Motion

Logo styles of interest
Pictorial/Combination Logo
Abstract Logo
Requirements
Should not have
• FLOWERS

```html
<!DOCTYPE html>
<html lang="en">
<head>
<meta charset="utf-8">
<title>Brightwell-Motion Business Cards</title>
<link rel="stylesheet" href="https://fonts.googleapis.com/css2?family=Alegreya:ital,wght@0,400;0,800;1,400&display=swap">
<style>
  :root {
    --paper: #ffffff;
    --divider: #000000;
    --ink-dark: #0a0a0a;
    --ink-mid: #444646;
    --ink-body: #3a3a3a;
    --mark-dark: #464848;
    --taupe-deep: #74665a;
    --taupe-light: #c1b39a;
  }
  * { margin: 0; padding: 0; box-sizing: border-box; }
  html, body {
    width: 1034px;
    height: 1200px;
    overflow: hidden;
    background: var(--paper);
  }
  body { font-family: "Alegreya", Georgia, serif; }
  .sheet { position: relative; width: 1034px; height: 1200px; }
  .card {
    position: absolute;
    left: 0;
    width: 1034px;
    height: 590px;
    background: var(--paper);
    overflow: hidden;
  }
  .card--mono { top: 0; }
  .card--taupe { top: 608px; height: 592px; }
  .divider {
    position: absolute;
    top: 590px;
    left: 0;
    width: 1034px;
    height: 18px;
    background: var(--divider);
  }
  .card__wash {
    position: absolute;
    right: 0;
    bottom: 0;
    width: 700px;
    height: 590px;
  }
  .card--mono .card__wash {
    background: radial-gradient(ellipse 90% 110% at 100% 100%,
      rgba(165, 212, 135, 0.75) 0%,
      rgba(190, 225, 170, 0.6) 40%,
      rgba(210, 235, 195, 0.35) 70%,
      rgba(255, 255, 255, 0) 100%);
  }
  .card--taupe .card__wash {
    background: radial-gradient(ellipse 90% 110% at 100% 100%,
      rgba(195, 228, 178, 0.6) 0%,
      rgba(210, 235, 198, 0.45) 40%,
      rgba(228, 242, 220, 0.3) 70%,
      rgba(255, 255, 255, 0) 100%);
  }
  .brand {
    position: absolute;
    left: 40px;
    top: 83px;
    width: 300px;
    text-align: center;
  }
  .brand__disc {
    display: block;
    width: 180px;
    height: 180px;
    border-radius: 50%;
    margin: 0 auto 26px;
  }
  .brand__name {
    font-weight: 800;
    font-size: 31px;
    line-height: 1.1;
  }
  .brand__strap {
    font-style: italic;
    font-size: 28px;
    line-height: 1.2;
    margin-top: 6px;
  }
  .address {
    position: absolute;
    left: 69px;
    top: 412px;
    font-size: 27px;
    line-height: 35px;
    font-style: normal;
  }
  .person {
    position: absolute;
    right: 68px;
    top: 76px;
    text-align: right;
  }
  .person__name {
    font-weight: 800;
    font-size: 60px;
    line-height: 1.1;
  }
  .person__role {
    font-size: 42px;
    line-height: 1.2;
    margin-top: 6px;
  }
  .contact {
    position: absolute;
    right: 68px;
    top: 410px;
    text-align: right;
    font-size: 25px;
    line-height: 35px;
    font-style: normal;
  }
  .contact a { color: inherit; text-decoration: none; }

  .card--mono .brand__disc { background: var(--mark-dark); }
  .card--mono .brand__name { color: var(--ink-dark); }
  .card--mono .brand__strap { color: var(--ink-mid); }
  .card--mono .address,
  .card--mono .contact { color: var(--ink-body); }
  .card--mono .person__name { color: var(--ink-dark); }
  .card--mono .person__role { color: var(--ink-mid); }

  .card--taupe .brand__disc { background: var(--taupe-light); }
  .card--taupe .brand__name { color: var(--taupe-deep); }
  .card--taupe .brand__strap { color: var(--taupe-light); }
  .card--taupe .address,
  .card--taupe .contact { color: var(--taupe-deep); }
  .card--taupe .person__name { color: var(--taupe-deep); }
  .card--taupe .person__role { color: var(--taupe-light); }
</style>
</head>
<body>
<main class="sheet">

  <section class="card card--mono">
    <div class="card__wash" role="img" aria-label="Soft green layered leaf-shaped background decoration"></div>
    <div class="brand">
      <span class="brand__disc"></span>
      <div class="brand__name">Brightwell-Motion</div>
      <div class="brand__strap">‘Move Stronger’</div>
    </div>
    <address class="address">
      212 Larkmore Street<br>
      Kelbridge<br>
      Vic 3261
    </address>
    <div class="person">
      <h1 class="person__name">Colette Farrow</h1>
      <p class="person__role">Remedial Massage Therapist</p>
    </div>
    <address class="contact">
      0417263950<br>
      <a href="mailto:info@brightwell-motion.com.au">info@brightwell-motion.com.au</a><br>
      <a href="https://www.brightwell-motion.com.au">www.brightwell-motion.com.au</a>
    </address>
  </section>

  <div class="divider"></div>

  <section class="card card--taupe">
    <div class="card__wash" role="img" aria-label="Pale green layered leaf-shaped background decoration"></div>
    <div class="brand">
      <span class="brand__disc"></span>
      <div class="brand__name">Brightwell-Motion</div>
      <div class="brand__strap">‘Move Stronger’</div>
    </div>
    <address class="address">
      212 Larkmore Street<br>
      Kelbridge<br>
      Vic 3261
    </address>
    <div class="person">
      <h2 class="person__name">Colette Farrow</h2>
      <p class="person__role">Remedial Massage Therapist</p>
    </div>
    <address class="contact">
      0417263950<br>
      <a href="mailto:info@brightwell-motion.com.au">info@brightwell-motion.com.au</a><br>
      <a href="https://www.brightwell-motion.com.au">www.brightwell-motion.com.au</a>
    </address>
  </section>

</main>
</body>
</html>
```